Business Cards

I'd like help creating business cards with the full logo "Veltrona Capital Partners" on the back of the card (navy background with white writing), and abbreviated logo "VCP" on the front. Would like to list name, title, phone number, email, and website listed on front of card. Would like to keep very simple. Front font Arial or similar.

```html
<!DOCTYPE html>
<html lang="en">
<head>
<meta charset="utf-8">
<title>Veltrona Capital Partners – Business Cards</title>
<link href="https://fonts.googleapis.com/css2?family=Arimo:wght@400;700&display=swap" rel="stylesheet">
<style>
  :root {
    --navy: #1c376a;
    --white: #ffffff;
    --paper: #ebebeb;
    --ink-grey: #3c3c3c;
    --rule: #4a5f8c;
  }
  * { box-sizing: border-box; margin: 0; padding: 0; }
  html, body { width: 1200px; height: 900px; overflow: hidden; }
  body {
    background: var(--paper);
    font-family: "Arimo", Arial, sans-serif;
    position: relative;
  }
  .card {
    position: absolute;
    width: 560px;
    height: 320px;
    top: 290px;
    box-shadow: 0 2px 6px rgba(0,0,0,0.12);
    overflow: hidden;
  }
  .card-back {
    left: 25px;
    background: var(--navy);
    color: var(--white);
    display: flex;
    flex-direction: column;
    align-items: center;
    justify-content: center;
  }
  .brand-name {
    font-size: 46px;
    font-weight: 700;
    letter-spacing: 1px;
    text-transform: uppercase;
    line-height: 1;
  }
  .brand-tagline {
    margin-top: 12px;
    font-size: 19px;
    font-weight: 700;
    letter-spacing: 7px;
    text-transform: uppercase;
  }
  .card-front {
    left: 615px;
    background: var(--white);
  }
  .front-mark {
    position: absolute;
    top: 42px;
    right: 40px;
    display: flex;
    align-items: center;
    gap: 12px;
    color: var(--navy);
  }
  .front-mark .mark-square {
    width: 16px;
    height: 16px;
    background: var(--navy);
  }
  .front-mark .mark-text {
    font-size: 52px;
    font-weight: 700;
    line-height: 1;
  }
  .divider {
    position: absolute;
    top: 134px;
    left: 30px;
    right: 30px;
    height: 1px;
    background: var(--rule);
  }
  .person {
    position: absolute;
    top: 148px;
    left: 34px;
  }
  .person-name {
    color: var(--navy);
    font-size: 25px;
    font-weight: 700;
    text-transform: uppercase;
    line-height: 1.1;
  }
  .person-title {
    color: var(--ink-grey);
    font-size: 15px;
    margin-top: 3px;
  }
  .person-rule {
    width: 170px;
    height: 1px;
    background: var(--rule);
    margin-top: 10px;
  }
  .contacts {
    list-style: none;
    margin-top: 8px;
  }
  .contacts li {
    display: flex;
    align-items: center;
    gap: 9px;
    color: var(--ink-grey);
    font-size: 14px;
    line-height: 20px;
  }
  .contacts svg { width: 13px; height: 13px; fill: var(--navy); flex: none; }
  .front-band {
    position: absolute;
    left: 0;
    right: 0;
    bottom: 0;
    height: 16px;
    background: var(--navy);
  }
</style>
</head>
<body>
  <section class="card card-back" aria-label="Card back">
    <div class="brand-name">Veltrona</div>
    <div class="brand-tagline">Capital Partners</div>
  </section>

  <section class="card card-front" aria-label="Card front">
    <div class="front-mark">
      <span class="mark-square"></span>
      <span class="mark-text">VCP</span>
    </div>
    <div class="divider"></div>
    <div class="person">
      <div class="person-name">Dorian Hale</div>
      <div class="person-title">CEO/Founder</div>
      <div class="person-rule"></div>
      <ul class="contacts">
        <li>
          <svg viewBox="0 0 16 16" aria-hidden="true"><path d="M3.5 1.5l2.5 0 1 3.5-1.8 1.2c.9 1.9 2.4 3.4 4.3 4.3l1.2-1.8 3.5 1v2.5c0 .9-.7 1.5-1.5 1.5C6.6 13.7 2.3 9.4 2 3c0-.8.6-1.5 1.5-1.5z"/></svg>
          (520)555-0147
        </li>
        <li>
          <svg viewBox="0 0 16 16" aria-hidden="true"><path d="M1 3.5h14v9H1z M1.5 4l6.5 5 6.5-5" fill="none" stroke="#1c376a" stroke-width="1.6"/></svg>
          info@veltronacapital.com
        </li>
        <li>
          <svg viewBox="0 0 16 16" aria-hidden="true"><circle cx="8" cy="8" r="6.5" fill="none" stroke="#1c376a" stroke-width="1.5"/><path d="M1.5 8h13M8 1.5c-2.4 2.2-2.4 10.8 0 13M8 1.5c2.4 2.2 2.4 10.8 0 13" fill="none" stroke="#1c376a" stroke-width="1.2"/></svg>
          www.veltronacapital.com
        </li>
      </ul>
    </div>
    <div class="front-band"></div>
  </section>
</body>
</html>
```